Brisko Web Design Project

My company is engaged in the provision of advertising service (mostly contextual advertising - like Pellix bidwords or Murelka vector) . The website must show the potential my customers that brisko company earnestly provide quality service, and design must be is in cheerful colors - also fashionable and brisko. very much needed positive illustrations showing what we are doing service in a positive and easy, based on trust and loyalty. Website should be similar to the clear and classic navigation, include links - home - about -services/portfolio -contacts. need to specify the hours of operation office and phone number + office address.

Target Market(s)

small/medium business

Industry/Entity Type

Advertising

Requirements
Must have
• it is important to understand that a lot depends on the quality of content - content design, it is worth special attention. and sure - the use of branded elements of the logo in the design of the site and details of the content. content should look modern, but it is understood and allowed a little classics. in general, I always like modern coupled with a combination of classic and fun and playful at the same time, serious intentions of consciousness.
Nice to have
• I'll add some links designs as an example that I like the web projects
http://www.norvatek.ru/context/
http://www.lupora.ru/services/kontekstnaja_reklama/
http://www.zekta.ru/context/
http://halmivex.ru/service/context/

So I need personal design, also nice and concise, with no extra bells and whistles. design must be based on the logo and colors of brisko combines a my logo. Font should be used is the same as in the logo. background should be white or light.
Should not have
• As usual - extraneous colors (not included in the logo as an attachment to the brief) fonts hard to read, there should be a lot of very dark tones and luscious colors with contrast. navigation and content must be easily understood by the user. I am sorry for my bad english, and I hope that u have an understanding of my description. if you want to clarify what else the details. before doing any work, please feel free to ask me to clarify.

```html
<!DOCTYPE html>
<html lang="en">
<head>
<meta charset="utf-8">
<title>Brisko — Contextual Advertising</title>
<link href="https://fonts.googleapis.com/css2?family=Source+Sans+3:ital,wght@0,400;0,600;0,700;1,400&display=swap" rel="stylesheet">
<style>
:root{
  --orange:#ef9c35;
  --orange-dark:#e0672a;
  --text:#5a5a5a;
  --heading:#3e3a36;
  --beige:#dcd4bc;
  --lime:#c3db3c;
  --sky:#8cc6d4;
  --sun:#f4c65c;
  --mint:#6fc09a;
  --pink:#e8808f;
  --teal:#3a9fb0;
  --footer:#6c6c6c;
  --white:#ffffff;
}
*{box-sizing:border-box;margin:0;padding:0}
html,body{width:720px;height:1200px;overflow:hidden}
body{position:relative;background:var(--white);font-family:"Source Sans 3",sans-serif;color:var(--text);font-size:8px}
h1,h2,h3{font-weight:400}
.abs{position:absolute}

.top-strip{left:0;top:0;width:720px;height:30px;background:#fafafa;border-bottom:1px solid #e8e8e8}
.search{left:462px;top:6px;width:166px;height:18px;background:#fff;border:1px solid #ddd}
.search svg{position:absolute;right:4px;top:2px}
.langs{left:642px;top:10px;font-size:8px;font-weight:700;color:#333}
.langs .on{color:var(--orange-dark)}

.header{left:0;top:30px;width:720px;height:92px;background:linear-gradient(#f7f7f7,#ececec)}
.brand{left:30px;top:52px;display:flex;align-items:center;gap:8px}
.brand-mark{width:34px;height:34px;background:var(--orange);border-radius:4px}
.brand-name{font-size:34px;font-weight:600;color:#4a3a2e;line-height:1}
.phones{left:384px;top:45px}
.phones p{font-size:11.5px;font-weight:600;color:var(--orange-dark);line-height:20.5px;padding-left:16px}
.phones p span{color:var(--orange)}
.phones svg{position:absolute;left:0;top:4px}
.info{left:578px;top:46px;font-size:8.5px;line-height:12px;color:#333}
.info .row{display:flex;gap:9px;margin-bottom:4px}
.info .val{color:var(--teal)}

.nav{left:0;top:122px;width:720px;height:30px;background:linear-gradient(var(--orange),#e99430)}
.nav a{position:absolute;top:9px;color:#fff;text-decoration:none;font-size:9.5px;line-height:12px}

.slider{left:30px;top:158px;width:468px;height:194px;background:var(--beige);border-radius:2px}
.slide{left:4px;top:5px;width:460px;height:186px;background:linear-gradient(100deg,#8a6a40 0%,#b6a57a 25%,#c5c56b 45%,#7a8a30 75%,#3e4a1e 100%)}
.slide-title{left:246px;top:44px;font-size:31px;font-weight:400;line-height:34px;color:#fff;letter-spacing:.5px;white-space:nowrap}
.slide-title .sub{color:#f4c04a;display:block}
.slide-text{left:246px;top:110px;width:196px;font-size:8.5px;line-height:13.5px;color:#fff}
.dots{left:403px;top:174px;display:flex;gap:4px}
.dots i{width:10px;height:10px;border-radius:50%;background:#ddd}
.dots i:first-child{background:var(--mint)}

.notes{left:504px;top:158px;width:186px;height:198px;background:var(--beige);border-radius:3px;padding:8px 10px}
.notes h3{font-size:14px;color:var(--heading)}
.note{position:absolute;left:10px;display:flex;gap:8px}
.date{width:36px;height:16px;background:var(--orange-dark);color:#fff;font-size:8.5px;text-align:center;line-height:16px;flex:none}
.note p{font-size:7.3px;line-height:12px;color:#444}
.read-all{position:absolute;left:10px;bottom:8px;font-size:8px;font-weight:700;color:var(--orange-dark)}

.h2{font-size:15px;color:var(--heading)}
.about{left:30px;top:370px;width:418px}
.about p{font-size:7.5px;line-height:13.6px;margin-top:4px}
.certs{left:463px;top:373px;width:227px}
.badge{left:466px;top:400px}
.cert-text{left:546px;top:399px;width:140px}
.cert-text b{font-size:8.5px;color:var(--teal);font-weight:600;display:block;margin-bottom:2px}
.cert-text p{font-size:7.5px;line-height:12px}

.tab{height:29px;padding:0 8px;font-size:14.5px;font-weight:400;line-height:29px;color:var(--heading);width:218px;white-space:nowrap;overflow:hidden}
.tab-line{height:6px}
.sec-context .tab{left:30px;top:490px;background:var(--lime)}
.sec-context .tab-line{left:30px;top:512px;width:660px;background:var(--lime)}
.ctx-text{left:30px;top:530px;width:385px;font-size:7.5px;line-height:13.6px}
.steps li{position:absolute;left:30px;list-style:none;display:flex;align-items:center;gap:10px;font-size:7.5px}
.steps .num{width:18px;height:18px;border-radius:50%;background:var(--orange-dark);color:#fff;font-size:9px;text-align:center;line-height:18px}
.results{left:430px;top:533px;width:258px;height:191px;background:linear-gradient(#f4f4f4,#e6ecf2);border:1px solid #ddd}

.sec-benefits .tab{left:30px;top:741px;background:var(--sky)}
.sec-benefits .tab-line{left:30px;top:763px;width:660px;background:var(--sky)}
.benefit{position:absolute;top:788px;width:120px;text-align:center}
.benefit svg{display:block;margin:0 auto;height:48px}
.benefit p{font-size:7.5px;line-height:12px;margin-top:10px;color:var(--text)}

.sec-reviews .tab{left:30px;top:904px;background:var(--sun)}
.sec-reviews .tab-line{left:30px;top:926px;width:468px;background:var(--sun)}
.review{position:absolute;top:948px;width:220px;font-size:7.2px;line-height:12px;font-style:italic}
.review .q{color:#e8b530;font-size:18px;font-weight:700;font-style:normal;line-height:8px;vertical-align:-5px;margin-right:3px}
.review b{display:block;margin-top:4px;font-weight:600}

.sec-conv .tab{left:30px;top:1014px;background:var(--mint)}
.sec-conv .tab-line{left:30px;top:1036px;width:468px;background:var(--mint)}
.ticks{position:absolute;top:1054px;list-style:none}
.ticks li{font-size:7.5px;line-height:15.6px;display:flex;gap:5px;align-items:center}

.order{left:510px;top:904px;width:180px;height:221px;background:var(--pink);border-radius:3px;padding:12px 14px}
.order h3{font-size:13px;color:#4a2a30;letter-spacing:.3px}
.field{position:absolute;left:14px;width:152px;height:21px;background:#fff;border:1px solid #f0b4bc;font-size:7.5px;color:#999;padding:4px 6px}
.submit{position:absolute;left:101px;top:190px;width:65px;height:20px;background:var(--lime);border:1px solid #8aa020;font-size:8px;font-weight:700;color:#3a4a10;text-align:center;line-height:18px}

.footer{left:0;top:1136px;width:720px;height:64px;background:var(--footer)}
.foot-brand{left:78px;top:1150px;display:flex;align-items:center;gap:6px}
.foot-brand .brand-mark{width:18px;height:18px;border-radius:2px}
.foot-brand span{font-size:17px;font-weight:600;color:#fff}
.copy{left:78px;top:1181px;font-size:7px;color:#eee}
.social{left:576px;top:1163px;display:flex;gap:8px}
.social i{width:18px;height:18px;background:#4a78b8;border-radius:2px}
.social i:last-child{background:#555}
</style>
</head>
<body>

<div class="abs top-strip"></div>
<div class="abs search"><svg width="14" height="14" viewBox="0 0 14 14"><circle cx="5.5" cy="5.5" r="4" fill="none" stroke="#e0672a" stroke-width="1.8"/><line x1="8.5" y1="8.5" x2="13" y2="13" stroke="#e0672a" stroke-width="2.2"/></svg></div>
<div class="abs langs">DE | <span class="on">EN</span> | RU</div>

<header class="abs header"></header>
<div class="abs brand"><div class="brand-mark"></div><div class="brand-name">Brisko</div></div>
<div class="abs phones">
  <svg width="10" height="11" viewBox="0 0 10 11"><rect x="0" y="0" width="10" height="11" rx="1.5" fill="#7a3020"/><rect x="2.5" y="2" width="5" height="2" fill="#fff"/></svg>
  <p>Moscow: <span>(123) 555 0142</span></p>
  <p>Kiev: <span>(123) 555 0142</span></p>
  <p>Novosibirsk: <span>(123) 555 0142</span></p>
</div>
<div class="abs info">
  <div class="row"><svg width="11" height="11" viewBox="0 0 11 11"><circle cx="5.5" cy="5.5" r="4.6" fill="none" stroke="#333"/><path d="M5.5 2.5V5.5H8" stroke="#333" fill="none"/></svg><div>Hours:<br><span class="val">Mon-Fri from 10:00 am</span></div></div>
  <div class="row"><svg width="11" height="9" viewBox="0 0 11 9"><rect x=".5" y=".5" width="10" height="8" fill="none" stroke="#333"/><path d="M.5 .5L5.5 5L10.5 .5" stroke="#333" fill="none"/></svg><div>Email:<br><span class="val">info@brisko.com</span></div></div>
</div>

<nav class="abs nav">
  <a style="left:30px">Home</a><a style="left:102px">About Us</a><a style="left:184px">Services</a><a style="left:268px">Portfolio</a><a style="left:350px">Customer Reviews</a><a style="left:478px">Stock</a><a style="left:550px">Latest News</a><a style="left:646px">Contact Us</a>
</nav>

<section class="abs slider">
  <div class="abs slide" role="img" aria-label="Photo of a red dart hitting the centre of a dartboard"></div>
  <h1 class="abs slide-title">CONTEXTUAL<span class="sub">ADVERTISING</span></h1>
  <p class="abs slide-text">Aliquam molestie, mi et imperdiet euismod, dui purus auctor tellus, et interdum lacus lectus et ante.</p>
  <div class="abs dots"><i></i><i></i><i></i><i></i></div>
</section>

<aside class="abs notes">
  <h3>Note:</h3>
  <div class="note" style="top:30px"><span class="date">08.18</span><p>Aenean a nibh eget turpis vehicula tempus ac sed massa. Vestibulum dolor nulla..</p></div>
  <div class="note" style="top:80px"><span class="date">08.18</span><p>Aenean a nibh eget turpis vehicula tempus ac sed massa. Vestibulum dolor nulla..</p></div>
  <div class="note" style="top:130px"><span class="date">08.18</span><p>Aenean a nibh eget turpis vehicula tempus ac sed massa. Vestibulum dolor nulla..</p></div>
  <a class="read-all">READ ALL</a>
</aside>

<section class="abs about">
  <h2 class="h2">About Our Company</h2>
  <p>Aliquam molestie, mi et imperdiet euismod, dui purus auctor tellus, et interdum lacus lectus et ante. Sed accumsan sollicitudin sapien, sit amet adipiscing turpis gravida ac. In congue, neque ac lobortis volutpat, libero mauris varius mi, vitae suscipit ipsum ligula vitae risus. Duis aliquam nibh a dui iaculis viverra id a velit. Vivamus egestas risus in magna varius commodo. Sed semper viverra egestas. Etiam pretium porttitor lectus, vel ornare neque porta volutpat.<br>Aenean a nibh eget turpis vehicula tempus ac sed massa. Vestibulum dolor nulla, ultrices ac tincidunt sed, laoreet non est. Suspendisse lobortis turpis in odio blandit ac interdum lorem euismod.</p>
</section>
<h2 class="abs h2 certs">Our certificates</h2>
<svg class="abs badge" width="72" height="82" viewBox="0 0 72 82"><path d="M0 0H72V58L36 82L0 58Z" fill="#f2b630"/><path d="M5 5H67V55L36 76L5 55Z" fill="#fff"/></svg>
<div class="abs cert-text"><b>CERTIFIED AGENCY</b><p>Companies that demonstrate a high level of work with Murelka. Directives and possessing ull-time certified experts in the field of selling content .</p></div>

<section class="sec-context">
  <h2 class="abs tab">What is Contextual Advertising</h2>
  <div class="abs tab-line"></div>
  <p class="abs ctx-text">Aliquam molestie, mi et imperdiet euismod, dui purus auctor tellus, et interdum lacus lectus et ante. Sed accumsan sollicitudin sapien, sit amet adipiscing turpis gravida ac. In congue, neque ac lobortis volutpat, libero mauris varius mi, vitae suscipit ipsum ligula vitae risus. Duis aliquam nibh a dui iaculis viverra id a velit. Vivamus egestas risus in magna varius commodo. Sed semper viverra egestas. Etiam pretium porttitor lectus, vel ornare neque porta volutpat. Nunc consequat congue nulla eu imperdiet.</p>
  <ul class="steps">
    <li style="top:608px"><span class="num">1</span>Sed semper viverra egestas. Etiam pretium porttitor lectus, vel ornare neque porta volutpat.</li>
    <li style="top:642px"><span class="num">2</span>Sed semper viverra egestas. Etiam pretium porttitor lectus, vel ornare neque porta volutpat.</li>
    <li style="top:676px"><span class="num">3</span>Sed semper viverra egestas. Etiam pretium porttitor lectus, vel ornare neque porta volutpat.</li>
  </ul>
  <div class="abs results" role="img" aria-label="Pellix search results page with ad blocks circled by hand in colour"></div>
</section>

<section class="sec-benefits">
  <h2 class="abs tab">Benefits of PPC Advertising</h2>
  <div class="abs tab-line"></div>
  <div class="benefit" style="left:32px"><svg viewBox="0 0 48 48" width="48"><circle cx="20" cy="20" r="11" fill="none" stroke="#333" stroke-width="4"/><line x1="28" y1="28" x2="42" y2="42" stroke="#333" stroke-width="6"/></svg><p>Vestibulum vel metus sit amet turpis bibendum tincidunt vel..</p></div>
  <div class="benefit" style="left:162px"><svg viewBox="0 0 48 48" width="48"><rect x="8" y="4" width="4" height="42" fill="#333"/><path d="M12 4H30L26 11L30 18H12Z" fill="#d22"/><rect x="26" y="14" width="3" height="32" fill="#333"/><path d="M29 14H44L40 20L44 26H29Z" fill="#333"/></svg><p>Vestibulum vel metus sit amet turpis bibendum tincidunt vel..</p></div>
  <div class="benefit" style="left:298px"><svg viewBox="0 0 80 48" width="80"><rect x="2" y="16" width="28" height="16" fill="#333"/><circle cx="16" cy="24" r="5" fill="#fff"/><text x="36" y="30" font-size="14" fill="#333" font-family="Source Sans 3,sans-serif">=</text><rect x="48" y="12" width="12" height="24" fill="#d22"/><text x="62" y="32" font-size="14" fill="#333" font-family="Source Sans 3,sans-serif">×N</text></svg><p>Vestibulum vel metus sit amet turpis bibendum tincidunt vel..</p></div>
  <div class="benefit" style="left:434px"><svg viewBox="0 0 48 48" width="48"><rect x="6" y="6" width="36" height="6" fill="#d22"/><rect x="6" y="18" width="36" height="4" fill="#333"/><rect x="6" y="27" width="36" height="4" fill="#333"/><rect x="6" y="36" width="36" height="4" fill="#333"/></svg><p>Vestibulum vel metus sit amet turpis bibendum tincidunt vel..</p></div>
  <div class="benefit" style="left:564px"><svg viewBox="0 0 48 48" width="48"><path d="M16 28L10 46L18 42L22 48L26 32Z" fill="#d22"/><path d="M32 28L38 46L30 42L26 48L22 32Z" fill="#d22"/><circle cx="24" cy="18" r="15" fill="#333"/><text x="24" y="21" font-size="9" fill="#fff" text-anchor="middle" font-family="Source Sans 3,sans-serif" font-weight="700">100%</text></svg><p>Vestibulum vel metus sit amet turpis bibendum tincidunt vel..</p></div>
</section>

<section class="sec-reviews">
  <h2 class="abs tab">Customer Reviews</h2>
  <div class="abs tab-line"></div>
  <div class="review" style="left:32px"><span class="q">“</span>Aenean a nibh eget turpis vehicula tempus ac sed massa. Vestibulum dolor nulla, ultrices ac tincidunt sed, laoreet non est...<b>Ltd. "Veltmor</b></div>
  <div class="review" style="left:276px"><span class="q">“</span>Aenean a nibh eget turpis vehicula tempus ac sed massa. Vestibulum dolor nulla, ultrices ac tincidunt sed, laoreet non est...<b>Ltd. "Veltmor</b></div>
</section>

<section class="sec-conv">
  <h2 class="abs tab">Increase Conversions</h2>
  <div class="abs tab-line"></div>
  <ul class="ticks" style="left:30px">
    <li><svg width="8" height="8" viewBox="0 0 8 8"><path d="M1 4L3 6.5L7 1" stroke="#e0672a" stroke-width="1.8" fill="none"/></svg>Sed semper viverra egestas.</li>
    <li><svg width="8" height="8" viewBox="0 0 8 8"><path d="M1 4L3 6.5L7 1" stroke="#e0672a" stroke-width="1.8" fill="none"/></svg>Etiam pretium porttitor lectus, vel ornare neque porta volutpat.</li>
    <li><svg width="8" height="8" viewBox="0 0 8 8"><path d="M1 4L3 6.5L7 1" stroke="#e0672a" stroke-width="1.8" fill="none"/></svg>Sed semper viverra egestas.</li>
    <li><svg width="8" height="8" viewBox="0 0 8 8"><path d="M1 4L3 6.5L7 1" stroke="#e0672a" stroke-width="1.8" fill="none"/></svg>Etiam pretium porttitor lectus, vel ornare neque porta volutpat.</li>
  </ul>
  <ul class="ticks" style="left:307px">
    <li><svg width="8" height="8" viewBox="0 0 8 8"><path d="M1 4L3 6.5L7 1" stroke="#e0672a" stroke-width="1.8" fill="none"/></svg>Sed semper viverra egestas.</li>
    <li><svg width="8" height="8" viewBox="0 0 8 8"><path d="M1 4L3 6.5L7 1" stroke="#e0672a" stroke-width="1.8" fill="none"/></svg>Etiam pretium porttitor lectus, vel ornare</li>
    <li><svg width="8" height="8" viewBox="0 0 8 8"><path d="M1 4L3 6.5L7 1" stroke="#e0672a" stroke-width="1.8" fill="none"/></svg>Sed semper viverra egestas.</li>
    <li><svg width="8" height="8" viewBox="0 0 8 8"><path d="M1 4L3 6.5L7 1" stroke="#e0672a" stroke-width="1.8" fill="none"/></svg>Etiam pretium porttitor lectus, vel ornare neque</li>
  </ul>
</section>

<form class="abs order">
  <h3>QUICK ORDER</h3>
  <div class="field" style="top:32px">Name</div>
  <div class="field" style="top:57px">Email Address</div>
  <div class="field" style="top:83px">Contact No</div>
  <div class="field" style="top:108px;height:73px">Type Message</div>
  <div class="submit">SUBMIT NOW</div>
</form>

<footer class="abs footer"></footer>
<div class="abs foot-brand"><div class="brand-mark"></div><span>Brisko</span></div>
<div class="abs copy">Copyright © 2013. All Right Reserved</div>
<div class="abs social"><i></i><i></i><i></i></div>

</body>
</html>
```